Industrial Company Profile Brochure Design

We need company profile brochure design. We are in industrial valve business and we are serving oil, petrochemical and power plants. We are working with our clients as trusted advisor. So, the final design should communicate valve solutions expert. The brochure should be 4 pages (including front and back) or folded style. However, it is open. We do not like to put any restriction on creativity. We leave the decision for number of pages and page size to the designer. The color theme should be same as / compatible with logo colors. You should use icons.Find attached the followings:- Our Logo- Word file that contains the required content (text and photos) for the brochure.3 Modern brochure designs. We like these designs. This is just to give you idea about what we like. The brochure is simple, clear and easy to get full information quickly.- Just banner for valve and components. You may need it.

Target Market(s)

The end users of oi, petrochemical and power plants

Industry/Entity Type

Engineering Consulting

Requirements
Must have
• - You must add our slogan. It is "Your Valves Solutions Expert"

```html
<!DOCTYPE html>
<html lang="en">
<head>
<meta charset="utf-8">
<title>Our Solutions – Halvern Process</title>
<link href="https://fonts.googleapis.com/css2?family=Fira+Sans:wght@300;400;800&family=Roboto:wght@300;400&display=swap" rel="stylesheet">
<style>
  :root {
    --orange: #f7941d;
    --cream: #fdf1e2;
    --peach: #fbe2c8;
    --mist: #f1f1f1;
    --mist-dark: #e4e4e4;
    --slogan-grey: #dcdcdc;
    --text: #3a3a3a;
    --heading: #6b6b6b;
    --line: #c9b8a6;
    --white: #ffffff;
  }
  * { margin: 0; padding: 0; box-sizing: border-box; }
  html, body { width: 849px; height: 1200px; overflow: hidden; background: var(--white); }
  .page {
    position: relative; width: 849px; height: 1200px; overflow: hidden;
    font-family: "Roboto", Arial, sans-serif; font-weight: 300; color: var(--text);
  }
  .backdrop { position: absolute; inset: 0; }
  .abs { position: absolute; }

  .section-title {
    position: absolute; left: 0; top: 0;
    transform: translate(37px, 466px) rotate(-90deg); transform-origin: left top;
    font-family: "Fira Sans", sans-serif; font-weight: 800; font-size: 50px;
    letter-spacing: 1px; color: var(--orange); line-height: 50px; white-space: nowrap;
  }
  .slogan {
    position: absolute; left: 0; top: 0; transform-origin: left top;
    font-family: "Fira Sans", sans-serif; font-weight: 400; white-space: nowrap;
  }
  .slogan-your { transform: translate(632px, 1160px) rotate(-90deg); font-size: 98px; line-height: 94px; color: var(--slogan-grey); }
  .slogan-main { transform: translate(722px, 1168px) rotate(-90deg); font-size: 112px; line-height: 108px; color: var(--slogan-grey); letter-spacing: -1px; }
  .slogan-main .accent { color: var(--peach); }

  .intro { left: 170px; top: 45px; width: 530px; font-size: 13.6px; line-height: 17.6px; text-align: justify; }
  .solution-heading { font-family: "Fira Sans", sans-serif; font-weight: 300; font-size: 31px; color: var(--heading); line-height: 34px; }
  .new-valves-heading { left: 170px; top: 158px; }
  .new-valves-text { left: 170px; top: 197px; width: 267px; font-size: 14px; line-height: 19px; text-align: justify; }
  .upgrade-heading { left: 170px; top: 646px; }
  .upgrade-text { left: 170px; top: 686px; width: 530px; font-size: 14px; line-height: 19px; text-align: justify; }
  .advantages { left: 170px; top: 743px; list-style: none; font-size: 14px; line-height: 19px; }
  .advantages li { padding-left: 22px; position: relative; }
  .advantages li::before { content: "•"; position: absolute; left: 0; }

  .media { position: absolute; }
  .framed { border: 1px solid #cfcfcf; }
</style>
</head>
<body>
<div class="page">
  <svg class="backdrop" width="849" height="1200" viewBox="0 0 849 1200" aria-hidden="true">
    <polygon points="0,0 240,0 150,560 0,760" fill="var(--cream)"/>
    <polygon points="240,0 420,0 150,560" fill="#fdf6ee"/>
    <polygon points="0,760 150,560 420,1200 0,1200" fill="#f7ece0"/>
    <polygon points="150,560 849,420 849,1200 420,1200" fill="var(--mist)"/>
    <polygon points="500,0 849,0 849,420 720,560" fill="#f6f6f6"/>
    <polygon points="720,560 849,420 849,1200 600,1200" fill="var(--mist-dark)" opacity="0.5"/>
    <line x1="120" y1="172" x2="120" y2="1200" stroke="var(--line)" stroke-width="1"/>
    <line x1="120" y1="172" x2="145" y2="172" stroke="var(--line)" stroke-width="1"/>
    <circle cx="145" cy="172" r="4" fill="var(--orange)"/>
    <line x1="62" y1="490" x2="120" y2="490" stroke="var(--line)" stroke-width="1"/>
    <circle cx="62" cy="490" r="4" fill="var(--orange)"/>
    <line x1="120" y1="662" x2="145" y2="662" stroke="var(--line)" stroke-width="1"/>
    <circle cx="145" cy="662" r="4" fill="var(--orange)"/>
  </svg>

  <div class="slogan slogan-your">your</div>
  <div class="slogan slogan-main"><span class="accent">valves</span> solutions expert</div>

  <h1 class="section-title">OUR SOLUTIONS</h1>

  <p class="abs intro">Halvern Process offers a full range of consultation services to help analyze your plant requirements for the effective implementation of solutions from our range of products. We cooperate with the end-user for a detailed analysis of the root cause and provide reliable solutions for different kinds of valve problems. Our products and services could be briefly divided into the following sections:</p>

  <h2 class="abs solution-heading new-valves-heading">New Valves</h2>
  <p class="abs new-valves-text">We provide consultation on and design of a variety of valves for different kinds of industrial applications. We have a rich set of valve designs and solutions available, providing solutions for severe service applications. For special valve solutions not available in the market, we can help our clients by manufacturing and delivering those valves in the shortest possible timeframe under the most complicated requirements.</p>

  <svg class="media" style="left:168px;top:200px" width="531" height="399" viewBox="0 0 531 399">
    <defs>
      <linearGradient id="cutawayTone" x1="0" y1="0" x2="1" y2="1">
        <stop offset="0" stop-color="#c9ccd0"/><stop offset="1" stop-color="#6f8192"/>
      </linearGradient>
      <linearGradient id="valvePhotoTone" x1="0" y1="0" x2="0" y2="1">
        <stop offset="0" stop-color="#d9dcdc"/><stop offset="0.45" stop-color="#c2c8c8"/><stop offset="1" stop-color="#5c6a6e"/>
      </linearGradient>
    </defs>
    <polygon role="img" aria-label="Cutaway rendering of a control valve trim" points="0,220 280,220 342,399 0,399" fill="url(#cutawayTone)"/>
    <polygon role="img" aria-label="Photograph of a large actuated control valve in a workshop" points="290,0 531,0 531,399 355,399 290,230" fill="url(#valvePhotoTone)"/>
  </svg>

  <h2 class="abs solution-heading upgrade-heading">Upgrade &amp; Retrofit</h2>
  <p class="abs upgrade-text">We supply highly reliable and efficient upgrading solutions for our clients, with the following key advantages:</p>
  <ul class="abs advantages">
    <li>Fits well into the existing valve</li>
    <li>Full responsibility of the valve</li>
    <li>Detailed documentation</li>
    <li>Saves the cost of piping modifications</li>
    <li>Lower installation costs</li>
    <li>Shorter plant downtime</li>
  </ul>

  <div class="media framed" role="img" aria-label="Product image of an electric valve actuator" style="left:168px;top:880px;width:221px;height:153px;background:linear-gradient(135deg,#f4f4f4,#b9bcc0)"></div>
  <div class="media" role="img" aria-label="Seal application guide cover" style="left:398px;top:878px;width:173px;height:87px;background:linear-gradient(180deg,#5a5a5a 0 30%,#b5601f 30%,#2a2a2a)"></div>
  <div class="media framed" role="img" aria-label="Product image of a valve sealing ring" style="left:398px;top:972px;width:173px;height:61px;background:linear-gradient(135deg,#f7f7f7,#b8b8b8)"></div>
  <div class="media" role="img" aria-label="Product image of a valve positioner unit" style="left:572px;top:757px;width:128px;height:276px;background:linear-gradient(90deg,#e0b21a 0 30%,#e9e9e9 30%,#cfcfcf)"></div>
  <div class="media framed" role="img" aria-label="Technical drawings of valve trim and anti-cavitation disc stacks" style="left:168px;top:1040px;width:469px;height:116px;background:linear-gradient(90deg,#ffffff 0 48%,#4a4a4a 48% 72%,#4aa64a 72% 94%,#ffffff 94%)"></div>
</div>
</body>
</html>
```